Tarrow Building Performance

Id like for my business card to be very bold and professional. Incorporating the business logo, the main services offered, and my contact info. Services are spray foam, insulation, new construction, retrofit, weatherization.

When opening this project sketch harbor was not able to upload my new logo that I picked from another recent sketch harbor project. Does anyone know how i could upload my logo onto the page for design of the business cards?

Target Market(s)

Building owners, contractors

Industry/Entity Type

Building Insulation and performance improvements

Contact Information for Business Card

Owner, Email dean@tarrowbuildingperformance.example Phone number 555-208-6147

Colors
0054AA
0677BA
7BADD7
CADEEF
E8F1F8
F0912C
F2A743
F7CA91
FBE8D2
FDF5EE

Requirements
Must have
• Services- spray foam, cellulose, mineral wool, fiberglass, air sealing, new construction, retrofit, weatherization, energy saving assesments

```html
<!DOCTYPE html>
<html lang="en">
<head>
<meta charset="utf-8">
<title>Tarrow Building Performance – Business Card</title>
<link rel="stylesheet" href="https://fonts.googleapis.com/css2?family=Montserrat:wght@700;800&family=Roboto:wght@400&family=Roboto+Condensed:wght@400&display=swap">
<style>
  :root {
    --backdrop: #e4e4e4;
    --card-white: #ffffff;
    --navy: #0b1433;
    --orange: #f07a22;
    --sky: #3cb4e6;
    --ink: #4a4a4a;
    --rule: #cfcfcf;
  }
  * { margin: 0; padding: 0; box-sizing: border-box; }
  html, body { width: 1200px; height: 1200px; overflow: hidden; }
  body { background: var(--backdrop); position: relative; font-family: "Roboto", Arial, sans-serif; }

  .card { position: absolute; width: 688px; height: 393px; overflow: hidden; box-shadow: 0 18px 26px rgba(0,0,0,.22); }
  .card--front { left: 256px; top: 159px; background: var(--card-white); }
  .card--back { left: 256px; top: 653px; background: var(--navy); }

  /* Front */
  .brand { position: absolute; display: flex; align-items: center; gap: 10px; }
  .brand__mark { width: 14px; height: 14px; background: var(--sky); flex: none; }
  .brand__name { font-family: "Montserrat", Arial, sans-serif; font-weight: 800; color: var(--orange); text-transform: uppercase; line-height: 1.1; white-space: nowrap; }
  .card--front .brand { left: 36px; top: 138px; width: 270px; }
  .card--front .brand__name { font-size: 16px; }

  .divider { position: absolute; left: 326px; top: 111px; width: 1.5px; height: 134px; background: var(--rule); }

  .person { position: absolute; left: 348px; top: 120px; }
  .person__name { font-family: "Montserrat", Arial, sans-serif; font-weight: 700; font-size: 26px; color: var(--orange); letter-spacing: .5px; line-height: 1; }
  .person__role { font-size: 15px; color: var(--sky); margin-top: 5px; }

  .contact { position: absolute; left: 348px; top: 193px; list-style: none; }
  .contact__item { display: flex; align-items: center; gap: 9px; font-size: 15px; color: var(--ink); line-height: 21px; white-space: nowrap; }
  .contact__icon { width: 13px; height: 13px; flex: none; }

  .footer-bar { position: absolute; left: 0; bottom: 0; width: 400px; height: 15px; background: var(--sky); }
  .footer-web { position: absolute; right: 0; bottom: 0; width: 316px; height: 33px; background: var(--orange);
    clip-path: polygon(24px 0, 100% 0, 100% 100%, 0 100%); display: flex; align-items: center; justify-content: center; padding-left: 22px;
    color: #fff; font-size: 15px; white-space: nowrap; }

  /* Back */
  .card--back .brand { left: 0; right: 0; top: 150px; justify-content: center; gap: 16px; }
  .card--back .brand__mark { width: 22px; height: 22px; }
  .card--back .brand__name { font-size: 34px; text-align: left; }

  .services { position: absolute; left: 0; right: 0; top: 327px; display: flex; justify-content: center; align-items: center; gap: 8px;
    font-family: "Roboto Condensed", Arial, sans-serif; font-size: 17.5px; color: #fff; list-style: none; text-transform: uppercase; white-space: nowrap; }
  .services__sep { width: 10px; height: 10px; flex: none; display: block; }
</style>
</head>
<body>

<section class="card card--front" aria-label="Business card front">
  <div class="brand">
    <span class="brand__mark"></span>
    <span class="brand__name">Tarrow<br>Building Performance</span>
  </div>

  <div class="divider"></div>

  <div class="person">
    <p class="person__name">MARK ELLERY</p>
    <p class="person__role">Owner</p>
  </div>

  <ul class="contact">
    <li class="contact__item">
      <svg class="contact__icon" viewBox="0 0 24 24" aria-hidden="true"><path fill="#f07a22" d="M6.6 10.8a15.1 15.1 0 0 0 6.6 6.6l2.2-2.2c.3-.3.7-.4 1-.2 1.1.4 2.3.6 3.6.6.6 0 1 .4 1 1V20c0 .6-.4 1-1 1A17 17 0 0 1 3 4c0-.6.4-1 1-1h3.5c.6 0 1 .4 1 1 0 1.2.2 2.4.6 3.6.1.3 0 .7-.2 1z"/></svg>
      555-208-6147
    </li>
    <li class="contact__item">
      <svg class="contact__icon" viewBox="0 0 24 24" aria-hidden="true"><rect x="2" y="5" width="20" height="14" fill="#f07a22"/><path d="M2 5l10 8 10-8" fill="none" stroke="#fff" stroke-width="2"/></svg>
      dean@tarrowbuildingperformance.example
    </li>
  </ul>

  <div class="footer-bar"></div>
  <div class="footer-web">tarrowbuildingperformance.example</div>
</section>

<section class="card card--back" aria-label="Business card back">
  <div class="brand">
    <span class="brand__mark"></span>
    <span class="brand__name">Tarrow<br>Building Performance</span>
  </div>

  <ul class="services">
    <li>Spray Foam</li>
    <li><svg class="services__sep" viewBox="0 0 10 10" aria-hidden="true"><g fill="#3cb4e6"><rect width="4" height="4"/><rect x="6" width="4" height="4"/><rect y="6" width="4" height="4"/><rect x="6" y="6" width="4" height="4"/></g></svg></li>
    <li>Insulation</li>
    <li><svg class="services__sep" viewBox="0 0 10 10" aria-hidden="true"><g fill="#3cb4e6"><rect width="4" height="4"/><rect x="6" width="4" height="4"/><rect y="6" width="4" height="4"/><rect x="6" y="6" width="4" height="4"/></g></svg></li>
    <li>New Construction</li>
    <li><svg class="services__sep" viewBox="0 0 10 10" aria-hidden="true"><g fill="#3cb4e6"><rect width="4" height="4"/><rect x="6" width="4" height="4"/><rect y="6" width="4" height="4"/><rect x="6" y="6" width="4" height="4"/></g></svg></li>
    <li>Retrofit</li>
    <li><svg class="services__sep" viewBox="0 0 10 10" aria-hidden="true"><g fill="#3cb4e6"><rect width="4" height="4"/><rect x="6" width="4" height="4"/><rect y="6" width="4" height="4"/><rect x="6" y="6" width="4" height="4"/></g></svg></li>
    <li>Weatherization.</li>
  </ul>
</section>

</body>
</html>
```